LumaLearn.net the Free Online Tutorial Needs a New Web Design

We need a new web design for our existing website, LumaLearn.net. We provide a Free Online Tutorial of any code, like HTML, CSS, PHP, Jquery, javascript etc, including online editor.
We would like to see designs that interesting, simple, interactive, and be a very comfortable place to read in a long time.
We need 2 pages design for:
1. Home Page (http://lumalearn.net) and
2. Listing Page (http://lumalearn.net/tutorial/833/sql/sql-basics/sql-and-or-operator.html)
For Listing Page We need nice "Left Menu" at left side and Content Page (min 728px) at right side.
I need File PSD and/or Vector Only, without HTML code.

```html
<!DOCTYPE html>
<html lang="en">
<head>
<meta charset="utf-8">
<title>LumaLearn.net – Free Online Tutorials</title>
<link href="https://fonts.googleapis.com/css2?family=Arimo:wght@400;700&display=swap" rel="stylesheet">
<style>
  :root{
    --black:#000;
    --ink:#333;
    --muted:#666;
    --soft:#999;
    --page:#f3f3f3;
    --white:#fff;
    --green:#6ab04c;
    --blue:#1a7fd1;
    --red:#f2504b;
    --tile:#f0f0f0;
    --dark:#2a2a2a;
    --footer-text:#8a8a8a;
    --rule:#3a3a3a;
  }
  *{box-sizing:border-box;margin:0;padding:0}
  html,body{width:1200px;height:1042px;overflow:hidden}
  body{position:relative;background:var(--page);font-family:"Arimo",Arial,sans-serif;color:var(--ink)}
  a{color:inherit;text-decoration:none}
  .abs{position:absolute}

  .topbar{left:0;top:0;width:1200px;height:69px;background:var(--black)}
  .brand{display:flex;align-items:center;gap:8px;color:var(--white);font-size:20px;font-weight:700}
  .brand-mark{width:20px;height:20px;background:var(--blue)}
  .site-brand{left:268px;top:17px}
  .signup{left:807px;top:20px;color:var(--white);font-size:10px;font-weight:700}
  .login{left:855px;top:15px;width:62px;height:23px;background:var(--green);color:var(--white);font-size:10px;font-weight:700;display:flex;align-items:center;justify-content:center;gap:7px}

  .hero{left:0;top:69px;width:1200px;height:316px;background:linear-gradient(100deg,#d8cfc8 0%,#f1ece8 30%,#e9e5e2 55%,#c9bfb8 80%,#ece8e5 100%)}
  .hero-title{left:0;top:198px;width:1184px;text-align:center;font-size:17px;color:#111}
  .store-badge{left:542px;top:233px;width:100px;height:30px;background:#111;border-radius:4px;border:1px solid #555}
  .dots{left:579px;top:322px;display:flex;gap:4px}
  .dots span{width:6px;height:6px;border-radius:50%;background:#222}
  .dots span:last-child{background:var(--blue)}

  .mainnav{left:268px;top:50px;width:649px;height:31px;background:var(--white);display:flex;align-items:center;font-size:8px;color:var(--muted)}
  .mainnav a{margin-left:19px;margin-right:18px;text-transform:uppercase}
  .mainnav a.active{color:var(--blue);position:relative}
  .mainnav a.active::before{content:"";position:absolute;left:0;right:0;top:-12px;height:2px;background:var(--blue)}
  .search{position:absolute;right:36px;top:7px;height:17px;border-left:1px solid #ccc;padding-left:10px}

  .panel{left:268px;top:344px;width:649px;height:287px;background:var(--white)}
  .intro{left:298px;top:366px;width:586px;height:94px;background:var(--red);color:var(--white);text-align:center}
  .intro h1{font-size:14px;font-weight:400;margin-top:19px}
  .intro p{font-size:7.6px;line-height:14px;margin:6px 48px 0}

  .featured-title{left:298px;top:478px;font-size:13.5px;font-weight:400;color:#444}
  .featured-desc{left:298px;top:504px;width:130px;font-size:7.6px;line-height:14px;color:var(--muted)}
  .view-all{left:299px;top:585px;font-size:7.6px;color:var(--muted);text-decoration:underline}

  .tiles{left:446px;top:481px;display:grid;grid-template-columns:repeat(4,104px);grid-auto-rows:55px;gap:7px 7.5px}
  .tile{background:var(--tile);text-align:center;color:#444}
  .tile b{display:block;font-size:14px;margin-top:10px;padding-bottom:5px;border-bottom:1px solid #ddd;margin-left:8px;margin-right:8px}
  .tile span{display:block;font-size:8px;margin-top:7px;color:var(--muted)}

  .tryit{left:268px;top:631px;width:649px;height:144px;background:var(--dark)}
  .tryit h2{position:absolute;left:30px;width:586px;top:13px;text-align:center;font-size:13.5px;font-weight:400;color:#ccc;padding-bottom:11px;border-bottom:1px solid #555}
  .try-cards{position:absolute;left:86px;top:59px;display:flex;gap:20px}
  .try-card{width:104px;height:55px;background:var(--white);text-align:center;color:#444}
  .try-card b{display:block;font-size:14px;margin-top:10px;padding-bottom:5px;border-bottom:1px solid #ddd;margin:10px 8px 0}
  .try-card span{display:block;font-size:8px;margin-top:7px;color:var(--muted)}
  .try-card.is-active{background:var(--green);color:var(--white)}
  .try-card.is-active b{border-color:rgba(255,255,255,.4)}
  .try-card.is-active span{color:var(--white)}

  .footer{left:0;top:804px;width:1200px;height:238px;background:var(--black);color:var(--footer-text)}
  .footer-nav{position:absolute;left:268px;top:14px;display:flex;gap:8px;font-size:7.6px}
  .footer-rule{position:absolute;left:268px;width:649px;height:1px;background:var(--rule)}
  .footer-col{position:absolute;top:59px;font-size:7.8px}
  .footer-col h3{font-size:10px;font-weight:400;color:#ccc;margin-bottom:15px}
  .footer-col li{list-style:none;line-height:14.3px}
  .footer-brand{left:821px;top:65px}
  .copyright{position:absolute;left:268px;top:216px;font-size:7.6px}
</style>
</head>
<body>
  <header class="abs topbar"></header>
  <a class="abs brand site-brand" href="http://lumalearn.net"><span class="brand-mark"></span>LumaLearn</a>
  <a class="abs signup" href="#">Sign Up</a>
  <a class="abs login" href="#">
    <svg width="9" height="10" viewBox="0 0 9 10"><rect x="0" y="4" width="9" height="6" fill="#333"/><path d="M2 4V3a2.5 2.5 0 0 1 5 0v1" fill="none" stroke="#333" stroke-width="1.4"/></svg>
    Login
  </a>

  <section class="abs hero" role="img" aria-label="Photo of students at a table reading a programming book"></section>
  <p class="abs hero-title">A Place for Learning and Trying of any Code</p>
  <div class="abs store-badge" role="img" aria-label="App store download badge"></div>
  <div class="abs dots"><span></span><span></span><span></span></div>

  <nav class="abs mainnav">
    <a class="active" href="#">Home</a>
    <a href="#">Our Tutorial Services</a>
    <a href="#">Try It</a>
    <a href="#">Web Tools</a>
    <a href="#">About Us</a>
    <span class="search"><svg width="10" height="10" viewBox="0 0 10 10"><circle cx="4" cy="4" r="3" fill="none" stroke="#222" stroke-width="1.5"/><path d="M6.2 6.2 9.5 9.5" stroke="#222" stroke-width="1.8"/></svg></span>
  </nav>

  <div class="abs panel"></div>
  <section class="abs intro">
    <h1>The Free Online Tutorials Place</h1>
    <p>LumaLearn is a place for Learning, testing, and examples for web building. The Examples in each chapter might be simplified to improve your basic understanding. With LumaLearn You will feel much easier than ever to learn about HTML including online code editor for each chapter, so you can edit, modify and execute the code.</p>
  </section>

  <h2 class="abs featured-title">Featured Tutorial</h2>
  <p class="abs featured-desc">Lorem Ipsum is simply dummy text of the printing and typesetting industry. Lorem Ipsum has been the industry's standard dummy</p>
  <a class="abs view-all" href="#">+ VIEW ALL TUTORIALS</a>

  <div class="abs tiles">
    <a class="tile" href="#"><b>&lt;HTML&gt;</b><span>HTML5 Tutorial</span></a>
    <a class="tile" href="#"><b>&lt;CSS&gt;</b><span>CSS Tutorial</span></a>
    <a class="tile" href="#"><b>&lt;JS&gt;</b><span>JavaScript Tutorial</span></a>
    <a class="tile" href="#"><b>&lt;PHP&gt;</b><span>PHP Tutorial</span></a>
    <a class="tile" href="#"><b>&lt;SQL&gt;</b><span>SQL Tutorial</span></a>
    <a class="tile" href="#"><b>&lt;JQUERY&gt;</b><span>JQUERY Tutorial</span></a>
    <a class="tile" href="#"><b>&lt;MYSQL&gt;</b><span>MYSQL Tutorial</span></a>
    <a class="tile" href="#"><b>&lt;JSON&gt;</b><span>JSON Tutorial</span></a>
  </div>

  <section class="abs tryit">
    <h2>Featured Try it Yourself</h2>
    <div class="try-cards">
      <a class="try-card is-active" href="#"><b>&lt;HTML5&gt;</b><span>TRY it Yourself</span></a>
      <a class="try-card" href="#"><b>&lt;CANVAS&gt;</b><span>TRY it Yourself</span></a>
      <a class="try-card" href="#"><b>&lt;SQL&gt;</b><span>TRY it Yourself</span></a>
      <a class="try-card" href="#"><b>&lt;EDITOR&gt;</b><span>TRY it Yourself</span></a>
    </div>
  </section>

  <footer class="abs footer">
    <nav class="footer-nav">
      <a href="#">Tutorial</a><a href="#">Articles</a><a href="#">Try it</a><a href="#">Canvas</a><a href="#">Webtools</a><a href="#">About</a><a href="#">Terms</a><a href="#">Privacy</a><a href="#">Disclaimer</a><a href="#">Contact</a><a href="#">FAQ</a>
    </nav>
    <div class="footer-rule" style="top:33px"></div>
    <div class="footer-col" style="left:268px">
      <h3>Site Links</h3>
      <ul><li>Random HTML5</li><li>Random Canvas</li><li>Random Javascript</li><li>Random Try it</li></ul>
    </div>
    <div class="footer-col" style="left:439px">
      <h3>Random Articles</h3>
      <ul><li>How to Make SQL Syntax Highlighter</li><li>Make A lot of Circle Animation on Canvas</li><li>Make A lot of Circle Animation on Canvas</li></ul>
    </div>
    <div class="footer-col" style="left:668px">
      <h3>Social Links</h3>
      <ul><li>Facelink</li><li>Chirper</li></ul>
    </div>
    <a class="brand footer-brand abs" href="http://lumalearn.net"><span class="brand-mark"></span>LumaLearn</a>
    <div class="footer-rule" style="top:202px"></div>
    <p class="copyright">LumaLearn © 2015, All rights reserved</p>
  </footer>
</body>
</html>
```